Kestrelwood Pathways Agency business cards

Australian company about to start offering its services. We recruit international students to come to study English, vocational education and postgraduate courses in Australia. We help them find the institution and select the right city they want to come to Australia. We are a young, online oriented and supportive agency. Our clients are between 18 and 35 years old, mainly University students, young professionals or people with work experience. We provide much more information that any other agency offer. We administrate a Facebook group with more than 11.000 members that daily ask questions about general information when coming to Australia, while they are here and even after they leave the country

Target Market(s)

International students from South America, Central America and Europe

Industry/Entity Type

Student

Contact Information for Business Card

Tomas Brevik
Managing Director
tomas@velmorin.com.au
www.velmorin.com.au
+61 491058263
Melbourne, Australia

Font styles to use
Serif
Sans Serif

Colors

Designer to choose colors to be used in the design.

Requirements
Must have
• Horizontal design
• Standard business card size and shape. If font uses green or yellow colours, they will have to match the ones from the logo
Nice to have
• UPDATE: Use the contents of the green image to design one of the card sides. Use our logo in the background of that side as watermark.
• Passport image, or immigration stamps. A picture of the Yarra River (from Melbourne) would be cool as well.
Should not have
• Non-standard business card size and shape
• Not black as the background colour of any sides as we are not a VIP agency or a hight class service. We are orientes to young people and they like colours, pictures, something attractive.
• Vertical design
• NO YELLOW or BLACK AS THE BACKGROUND COLOUR OF ANY SIDE OF THE BIZ CARD

```html
<!DOCTYPE html>
<html lang="en">
<head>
<meta charset="utf-8">
<title>Kestrelwood Pathways Agency – Business Cards</title>
<link href="https://fonts.googleapis.com/css2?family=Open+Sans:wght@400;600&display=swap" rel="stylesheet">
<style>
  :root {
    --backdrop: #5b6366;
    --card-yellow: #e6bc22;
    --card-white: #ffffff;
    --brand-green: #0f6b45;
    --brand-green-dark: #0a4f33;
    --ink: #1d1d1d;
    --shadow: rgba(0, 0, 0, 0.35);
  }
  * { margin: 0; padding: 0; box-sizing: border-box; }
  html, body {
    width: 1200px; height: 900px; overflow: hidden;
    background: var(--backdrop);
    font-family: "Open Sans", Arial, sans-serif;
  }
  .canvas { position: relative; width: 1200px; height: 900px; }
  .card {
    position: absolute; left: 290px;
    width: 620px; height: 354px;
    box-shadow: 0 10px 24px var(--shadow);
    overflow: hidden;
  }
  .card--front { top: 60px; background: var(--card-white); }
  .card--back { top: 486px; background: var(--card-white); }

  /* Front */
  .front-brand {
    position: absolute; left: 0; right: 0; top: 120px;
    display: flex; align-items: center; justify-content: center; gap: 16px;
  }
  .brand-dot {
    width: 34px; height: 34px; border-radius: 50%;
    background: var(--card-yellow);
  }
  .brand-name {
    font-weight: 600; font-size: 62px; line-height: 1;
    color: var(--brand-green); letter-spacing: 0.5px;
  }
  .front-web {
    position: absolute; left: 34px; bottom: 26px;
    color: var(--brand-green); font-size: 17px;
  }

  /* Back */
  .back-shapes { position: absolute; inset: 0; }
  .back-brand {
    position: absolute; left: 110px; top: 38px;
    display: flex; align-items: center; gap: 10px;
  }
  .back-brand .brand-dot { width: 22px; height: 22px; }
  .back-brand .brand-name { font-size: 40px; }
  .contact-list {
    position: absolute; left: 30px; top: 148px;
    list-style: none; font-size: 15px; color: var(--ink);
  }
  .contact-item {
    display: flex; align-items: center; gap: 10px; margin-bottom: 9px;
  }
  .contact-icon {
    width: 20px; height: 20px; background: var(--brand-green);
    display: flex; align-items: center; justify-content: center;
  }
  .name-block {
    position: absolute; left: 420px; top: 42px; width: 190px;
    color: var(--card-white);
  }
  .person-name { font-size: 24px; font-weight: 400; line-height: 1.1; }
  .person-title { font-size: 11px; margin-top: 4px; }
  .city-badge {
    position: absolute; left: 440px; top: 196px;
    width: 70px; height: 70px; border-radius: 50%;
    background: var(--ink);
    border: 5px solid var(--card-yellow);
    box-shadow: 0 0 0 2px var(--ink);
  }
  .city {
    position: absolute; left: 400px; top: 292px;
    font-size: 16px; color: var(--ink);
  }
</style>
</head>
<body>
<main class="canvas">

  <section class="card card--front" aria-label="Card front">
    <div class="front-brand">
      <span class="brand-dot"></span>
      <span class="brand-name">Velmorin</span>
    </div>
    <p class="front-web">www.velmorin.com.au</p>
  </section>

  <section class="card card--back" aria-label="Card back">
    <svg class="back-shapes" width="620" height="354" viewBox="0 0 620 354" aria-hidden="true">
      <polygon points="400,0 620,0 620,354 330,354" fill="var(--card-yellow)"/>
      <polygon points="392,36 420,28 420,112 370,112" fill="var(--brand-green-dark)"/>
      <rect x="410" y="28" width="210" height="86" fill="var(--brand-green)"/>
    </svg>

    <div class="back-brand">
      <span class="brand-dot"></span>
      <span class="brand-name">Velmorin</span>
    </div>

    <ul class="contact-list">
      <li class="contact-item">
        <span class="contact-icon">
          <svg width="12" height="12" viewBox="0 0 24 24"><path fill="#fff" d="M6.6 10.8a15 15 0 0 0 6.6 6.6l2.2-2.2a1 1 0 0 1 1-.25 11.4 11.4 0 0 0 3.6.57 1 1 0 0 1 1 1V20a1 1 0 0 1-1 1A17 17 0 0 1 3 4a1 1 0 0 1 1-1h3.5a1 1 0 0 1 1 1c0 1.25.2 2.450.57 3.57a1 1 0 0 1-.25 1z"/></svg>
        </span>+61 491058263
      </li>
      <li class="contact-item">
        <span class="contact-icon">
          <svg width="12" height="12" viewBox="0 0 24 24"><rect x="2" y="5" width="20" height="14" fill="none" stroke="#fff" stroke-width="2"/><path d="M2 5l10 8 10-8" fill="none" stroke="#fff" stroke-width="2"/></svg>
        </span>tomas@velmorin.com.au
      </li>
      <li class="contact-item">
        <span class="contact-icon">
          <svg width="12" height="12" viewBox="0 0 24 24"><circle cx="12" cy="12" r="9" fill="none" stroke="#fff" stroke-width="2"/><path d="M3 12h18M12 3c3 3 3 15 0 18M12 3c-3 3-3 15 0 18" fill="none" stroke="#fff" stroke-width="1.6"/></svg>
        </span>www.velmorin.com.au
      </li>
    </ul>

    <div class="name-block">
      <p class="person-name">Tomas Brevik</p>
      <p class="person-title">Managing Director</p>
    </div>

    <div class="city-badge" role="img" aria-label="City badge"></div>
    <p class="city">Melbourne, Australia</p>
  </section>

</main>
</body>
</html>
```